Harlow Custom Craft Website update

I would like an updated website to my current site (Harlowcraft.com).
I have an updated logo i would like to incorporate.
24 pages , would like to integrate videos of the boats (that i can upload later)

Target Market(s)

Professional and Commercial boat owners

Industry/Entity Type

Custom Boat Manufacturing

Coding

Coded - Design and coding required

Number of Pages Required

5+ page

Font styles to use
Serif

Requirements
Must have
• Easy to read, well laid-out, and video integration
Nice to have
• Fresh up to date look

```html
<!DOCTYPE html>
<html lang="en">
<head>
<meta charset="utf-8">
<title>Harlow Custom Craft</title>
<link href="https://fonts.googleapis.com/css2?family=Playfair+Display:wght@400;700&family=Open+Sans:wght@400;600;700&display=swap" rel="stylesheet">
<style>
:root{
  --red:#c4262c;
  --blue:#1b3f8f;
  --navy:#1d3554;
  --ink:#222;
  --muted:#666;
  --black:#0b0b0b;
  --cream:#eeece6;
  --white:#fff;
}
*{box-sizing:border-box;margin:0;padding:0}
html,body{width:1200px;height:3704px;overflow:hidden}
body{font-family:"Open Sans",sans-serif;color:var(--ink);background:var(--white);position:relative}
section,header,footer{position:absolute;left:0;width:1200px}

/* hero */
.hero{top:0;height:640px;background:linear-gradient(160deg,#5d8aa4 0%,#2f5a78 40%,#163247 100%);color:var(--white);overflow:hidden}
.topbar{height:40px;background:rgba(0,0,0,.55);display:flex;align-items:center;gap:28px;padding-left:160px;font-size:12px}
.nav{height:70px;display:flex;align-items:center;justify-content:space-between;padding:0 160px}
.brand{display:flex;align-items:center;gap:10px;font-family:"Playfair Display",serif;font-weight:700;font-size:22px;color:var(--white)}
.brand i{width:14px;height:14px;background:var(--red);display:block}
.menu{display:flex;gap:6px;font-size:12px;font-weight:600}
.menu a{color:var(--white);text-decoration:none;padding:10px 16px}
.menu a.on{background:var(--red)}
.hero-copy{position:absolute;left:100px;top:230px;width:720px}
.hero-copy h1{font-family:"Playfair Display",serif;font-size:50px;line-height:1.08;font-weight:700;text-transform:uppercase}
.hero-copy p{font-size:16px;line-height:1.55;margin:22px 0 30px;font-weight:600;width:560px}
.btn{display:inline-block;background:var(--red);color:var(--white);font-size:12px;font-weight:700;padding:12px 24px;text-transform:uppercase}
.btn-dark{background:rgba(0,0,0,.55);border:1px solid rgba(255,255,255,.5)}
.dots{position:absolute;left:0;right:0;top:590px;display:flex;justify-content:center;gap:10px}
.dots span{width:12px;height:12px;border-radius:50%;border:2px solid var(--white)}
.dots span.on{background:var(--red);border-color:var(--red)}

/* about */
.about{top:640px;height:688px;text-align:center}
.eyebrow{font-size:14px;letter-spacing:1px;text-transform:uppercase;color:var(--ink)}
.title{font-family:"Playfair Display",serif;font-weight:700;font-size:46px;color:var(--blue);text-transform:uppercase;line-height:1.1}
.subtitle{font-family:"Playfair Display",serif;font-size:22px;color:var(--red);text-transform:uppercase}
.about .eyebrow{margin-top:78px}
.about .title{margin-top:18px}
.about-text{width:880px;margin:50px auto 0;font-size:15px;line-height:1.75;color:#444}
.about .btn{margin-top:40px}
.stats{display:flex;justify-content:center;gap:110px;margin-top:66px}
.stat b{display:block;font-family:"Playfair Display",serif;font-size:48px;font-weight:400}
.stat span{font-size:12px;text-transform:uppercase;color:#444}

/* gallery */
.gallery{top:1328px;height:492px;display:flex;gap:12px}
.gallery div{height:492px}
.g1{width:220px;background:linear-gradient(#b9cfe0,#3f6d95)}
.g2{width:668px;background:linear-gradient(#4f9fc9 0%,#2a8e7f 45%,#33b6b8 70%,#1c6f7e 100%)}
.g3{width:288px;background:linear-gradient(#d9d3c7,#8a7e6d)}
.arrow{position:absolute;top:226px;width:40px;height:40px;background:rgba(0,0,0,.45);display:flex;align-items:center;justify-content:center}

/* featured */
.featured{top:1820px;height:820px;text-align:center}
.featured .eyebrow{margin-top:84px}
.featured .title{margin-top:14px}
.cards{display:flex;justify-content:center;gap:20px;margin-top:50px;text-align:left}
.card{width:290px;border:1px solid #ddd;padding:10px;background:var(--white)}
.card-img{height:200px;background:linear-gradient(#9fb9cf,#4d6c84)}
.card h3{font-family:"Playfair Display",serif;font-size:17px;color:var(--blue);margin:14px 0 10px;font-weight:400}
.specs{display:grid;grid-template-columns:1fr 1fr;gap:4px 10px;font-size:10px;color:var(--muted)}
.specs b{color:var(--blue);font-weight:600}
.card-foot{display:flex;justify-content:space-between;align-items:end;border-top:1px solid #eee;margin-top:14px;padding-top:10px}
.price small{display:block;font-size:10px;color:var(--muted)}
.price b{font-size:22px;color:var(--red)}
.view{background:var(--blue);color:var(--white);font-size:10px;font-weight:700;padding:9px 14px}
.fdots{display:flex;justify-content:center;gap:10px;margin-top:36px}
.fdots span{width:9px;height:9px;border-radius:50%;background:#ccc}
.fdots span.on{background:var(--white);border:2px solid var(--red)}

/* video */
.video{top:2640px;height:520px;background:linear-gradient(180deg,#2e5776,#1d3554 50%,#17283d);color:var(--white)}
.video-copy{position:absolute;left:160px;top:150px;width:440px}
.video-copy .eyebrow{color:var(--white);font-size:12px}
.video-copy h2{font-family:"Playfair Display",serif;font-size:40px;white-space:nowrap;text-transform:uppercase;margin:6px 0 10px;font-weight:700}
.video-copy p{font-size:14px;line-height:1.7;margin:16px 0 34px;color:#dbe3ea;width:400px}
.player{position:absolute;left:640px;top:120px;width:460px;height:300px;background:linear-gradient(170deg,#8fb0c8,#385a77 60%,#22384f)}
.play{position:absolute;left:190px;top:110px;width:80px;height:80px;border-radius:50%;background:var(--white);display:flex;align-items:center;justify-content:center}

/* newsletter */
.news{top:3160px;height:120px;background:var(--cream);display:flex;align-items:center;padding-left:272px;gap:18px}
.news .field{width:290px;height:48px;background:var(--white);font-size:12px;color:#999;padding:16px}
.news .btn{padding:16px 44px;font-size:13px}
.follow{font-size:13px;font-weight:600;margin-left:14px;display:flex;align-items:center;gap:12px}
.follow i{width:24px;height:24px;border-radius:50%;background:#333;display:block}

/* footer */
.footer{top:3280px;height:424px;background:var(--black);color:#ccc}
.f-brand{position:absolute;left:160px;top:56px;width:260px}
.f-brand p{font-size:12px;line-height:1.7;margin-top:22px}
.f-social{display:flex;gap:10px;margin-top:26px}
.f-social i{width:26px;height:26px;border-radius:50%;background:var(--red);display:block}
.f-col{position:absolute;top:52px}
.f-col h4{font-family:"Playfair Display",serif;font-size:26px;color:var(--white);font-weight:400;margin-bottom:22px}
.f-col li{list-style:none;font-size:13px;line-height:1.9;display:flex;align-items:center;gap:10px}
.f-col li::before{content:"";width:4px;height:4px;background:var(--red)}
.f-col.contact li::before{display:none}
.copy{position:absolute;bottom:0;left:0;right:0;height:44px;border-top:1px solid #222;display:flex;align-items:center;justify-content:center;font-size:11px;color:#888}
</style>
</head>
<body>

<header class="hero" role="img" aria-label="Custom boat cruising open water at sunset, seen from the deck">
  <div class="topbar">
    <span>1420 Harbor Rd, Bayport, Louisiana 70999</span>
    <span>985-555-0148</span>
    <span>support@harlowcraft.com</span>
  </div>
  <nav class="nav">
    <div class="brand"><i></i>Harlow Custom Craft</div>
    <div class="menu">
      <a class="on">HOME</a><a>ABOUT US</a><a>OUR BOATS</a><a>OPTIONAL EQUIPMENT</a><a>CONTACT</a>
    </div>
  </nav>
  <div class="hero-copy">
    <h1>Modern and First<br>Class Custom Boats</h1>
    <p>Our Harlow Dive Specials are especially designed for dive operators and dive enthusiasts alike. From our custom dive tank holders, water entry platforms, camera tables.</p>
    <span class="btn btn-dark">Just Click Here</span>
  </div>
  <div class="dots"><span></span><span class="on"></span><span></span><span></span></div>
</header>

<section class="about">
  <p class="eyebrow">About Us</p>
  <h2 class="title">Welcome to Harlow Boats</h2>
  <p class="subtitle">We build custom boats to meet our customers' specification</p>
  <p class="about-text">Welcome to Harlow Boats. We build custom boats to meet our customers' specification. Our boats range in size from 26' to 71'. We specialize in Dive Boats, Yachts Sport Fishermen, Patrol Boats, and Research Vessels. Our projects are original and diverse. Quality and customer satisfaction are always our top priorities. Our Harlow Dive Specials are especially designed for dive operators and dive enthusiasts alike. From our custom dive tank holders, water entry platforms, camera tables, fresh water rinse showers, ample deck space and much more.</p>
  <span class="btn">Discover More</span>
  <div class="stats">
    <div class="stat"><b>1254</b><span>Satisfied clients with our services</span></div>
    <div class="stat"><b>100+</b><span>Experienced crew</span></div>
    <div class="stat"><b>300+</b><span>Custom boats built</span></div>
    <div class="stat"><b>100+</b><span>Premium facilities</span></div>
  </div>
</section>

<section class="gallery">
  <div class="g1" role="img" aria-label="White boat moored near a coastal town"></div>
  <div class="g2" role="img" aria-label="Yacht anchored in a turquoise tropical bay"></div>
  <div class="g3" role="img" aria-label="Boat deck with lounge seating"></div>
  <span class="arrow" style="left:0"><svg width="12" height="12" viewBox="0 0 12 12"><path d="M8 1 3 6l5 5" fill="none" stroke="#fff" stroke-width="2"/></svg></span>
  <span class="arrow" style="right:0"><svg width="12" height="12" viewBox="0 0 12 12"><path d="m4 1 5 5-5 5" fill="none" stroke="#fff" stroke-width="2"/></svg></span>
</section>

<section class="featured">
  <p class="eyebrow">Our Boats</p>
  <h2 class="title">Featured Custom Boats</h2>
  <div class="cards">
    <article class="card">
      <div class="card-img" role="img" aria-label="37 foot custom dive boat at the dock"></div>
      <h3>37' Custom Dive</h3>
      <div class="specs">
        <span>Vessel <b>Custom</b></span><span>Year <b>2024</b></span>
        <span>Fuel Capacity <b>360</b></span><span>Horse Power <b>560</b></span>
        <span>Fuel Type <b>Diesel</b></span><span>Hull Draft <b>3.0'</b></span>
        <span>Engine <b>Twin</b></span><span>Max Capacity <b>1500</b></span>
        <span>Weight <b>8 lbs</b></span><span>Length <b>37 ft</b></span>
      </div>
      <div class="card-foot"><div class="price"><small>Price From</small><b>$7,659,000</b></div><span class="view">VIEW MORE</span></div>
    </article>
    <article class="card">
      <div class="card-img" role="img" aria-label="38 foot dive special boat on calm water"></div>
      <h3>38' Dive Specials</h3>
      <div class="specs">
        <span>Vessel <b>Custom</b></span><span>Year <b>2024</b></span>
        <span>Fuel Capacity <b>400</b></span><span>Horse Power <b>600</b></span>
        <span>Fuel Type <b>Diesel</b></span><span>Hull Draft <b>3.2'</b></span>
        <span>Engine <b>Twin</b></span><span>Max Capacity <b>1600</b></span>
        <span>Weight <b>9 lbs</b></span><span>Length <b>38 ft</b></span>
      </div>
      <div class="card-foot"><div class="price"><small>Price From</small><b>$7,659,000</b></div><span class="view">VIEW MORE</span></div>
    </article>
    <article class="card">
      <div class="card-img" role="img" aria-label="40 foot research vessel beside trees"></div>
      <h3>40' Research Vessel</h3>
      <div class="specs">
        <span>Vessel <b>Custom</b></span><span>Year <b>2024</b></span>
        <span>Fuel Capacity <b>450</b></span><span>Horse Power <b>700</b></span>
        <span>Fuel Type <b>Diesel</b></span><span>Hull Draft <b>3.5'</b></span>
        <span>Engine <b>Twin</b></span><span>Max Capacity <b>1800</b></span>
        <span>Weight <b>10 lbs</b></span><span>Length <b>40 ft</b></span>
      </div>
      <div class="card-foot"><div class="price"><small>Price From</small><b>$7,659,000</b></div><span class="view">VIEW MORE</span></div>
    </article>
  </div>
  <div class="fdots"><span class="on"></span><span></span><span></span><span></span><span></span></div>
</section>

<section class="video">
  <div class="video-copy">
    <p class="eyebrow">Media</p>
    <h2>Watch Our Videos</h2>
    <p>See our custom boats in action on the water. Walk through decks, helms and dive platforms, and watch our crews test every hull before delivery to owners.</p>
    <span class="btn">View Gallery</span>
  </div>
  <div class="player" role="img" aria-label="Video still of a boat deck facing the sea">
    <span class="play"><svg width="26" height="30" viewBox="0 0 26 30"><path d="M2 1l23 14L2 29z" fill="#1d3554"/></svg></span>
  </div>
</section>

<section class="news">
  <span class="field">Your email</span>
  <span class="btn">Subscribe</span>
  <span class="follow">Follow us <i></i><i></i><i></i><i></i></span>
</section>

<footer class="footer">
  <div class="f-brand">
    <div class="brand"><i></i>Harlow Custom Craft</div>
    <p>If you don't see what you are looking for, call. We can customize your boat to suit your needs. Call us today at 985-555-0148. 1420 Harbor Rd, Bayport, Louisiana 70999</p>
    <div class="f-social"><i></i><i></i><i></i><i></i></div>
  </div>
  <div class="f-col" style="left:500px">
    <h4>Explore</h4>
    <ul><li>Home</li><li>US Coast Guard Package</li><li>Contact Us</li><li>FAQ</li><li>Driving Directions</li><li>Terms &amp; Conditions</li><li>Privacy Policy</li></ul>
  </div>
  <div class="f-col contact" style="left:760px">
    <h4>Contact Us</h4>
    <ul><li>1420 Harbor Rd, Bayport, Louisiana 70999</li><li>985-555-0148</li><li>support@harlowcraft.com</li></ul>
  </div>
  <div class="copy">Harlow Boats Inc. &copy; All Rights Reserved - 2024</div>
</footer>

</body>
</html>
```